ALL TEXT GRAPHICS TM May 2025 for Instagram

We are looking for a series of social media graphics for Instagram (new size: 4:5 (1080 x 1350 pixels) ratio that are ALL TEXT. We want the following quotes below on each graphic; one quote per graphic. AND, In very small letters at the bottom of each graphic, add @TovaMarshOnline
The look and feel of these graphics should be complimentary to the color palette attached below; but keep them simple. But the design is up to you; at the end of this document, I provided various samples of all text graphics that I like as examples.
Target Market(s)
women looking to lose weight
Look and feel

```html
<!DOCTYPE html>
<html lang="en">
<head>
<meta charset="utf-8">
<title>All Text Graphics — Tova Marsh</title>
<link rel="stylesheet" href="https://fonts.googleapis.com/css2?family=Archivo:wght@500;600&family=Open+Sans:wdth,wght@80,500;80,600&family=Crimson+Text:wght@400&display=swap">
<style>
  :root {
    --backdrop: #000000;
    --card: #ffffff;
    --ink: #d4006e;
  }
  * { margin: 0; padding: 0; box-sizing: border-box; }
  html, body {
    width: 1200px;
    height: 609px;
    overflow: hidden;
    background: var(--backdrop);
  }
  .sheet {
    position: relative;
    width: 1200px;
    height: 609px;
  }
  .post {
    position: absolute;
    width: 224px;
    height: 280px;
    background: var(--card);
    color: var(--ink);
  }
  .quote {
    position: absolute;
    left: 0;
    right: 0;
    top: 133px;
    transform: translateY(-50%);
    text-align: center;
    font-family: "Archivo", Arial, sans-serif;
    font-weight: 500;
    line-height: 0.98;
    letter-spacing: -0.02em;
    white-space: nowrap;
    text-transform: uppercase;
  }
  .quote--humanist {
    font-family: "Open Sans", Arial, sans-serif;
    font-stretch: 80%;
    font-weight: 500;
    letter-spacing: 0;
  }
  .quote span { display: block; }
  .handle {
    position: absolute;
    left: 0;
    right: 0;
    top: 237px;
    text-align: center;
    font-family: "Crimson Text", Georgia, serif;
    font-size: 7.5px;
    letter-spacing: 0.02em;
    text-transform: uppercase;
  }
  .col-1 { left: 15px; }
  .col-2 { left: 252px; }
  .col-3 { left: 490px; }
  .col-4 { left: 727px; }
  .col-5 { left: 961px; }
  .row-1 { top: 11px; }
  .row-2 { top: 304px; }
</style>
</head>
<body>
<main class="sheet">

  <article class="post row-1 col-1">
    <p class="quote">
      <span style="font-size:14.4px">Tired. Moody.</span>
      <span style="font-size:22px">Stubborn</span>
      <span style="font-size:21px">Belly Fat.</span>
      <span style="font-size:14px">Your Hormones</span>
      <span style="font-size:14px">Are Screaming</span>
      <span style="font-size:21px">For Help!</span>
      <span style="font-size:13px">Let’s Fix That.</span>
    </p>
    <p class="handle">@TovaMarshOnline</p>
  </article>

  <article class="post row-1 col-2">
    <p class="quote">
      <span style="font-size:15.5px">What Worked</span>
      <span style="font-size:18px">In Your 30s</span>
      <span style="font-size:12.5px">Won’t Work Now.</span>
      <span style="font-size:16.5px">Here’s What</span>
      <span style="font-size:14px">Actually Does.</span>
      <span style="font-size:13px">Drop 30 Pounds</span>
      <span style="font-size:16px">In 3 Months.</span>
    </p>
    <p class="handle">@TovaMarshOnline</p>
  </article>

  <article class="post row-1 col-3">
    <p class="quote">
      <span style="font-size:13.8px">This Is The Secret</span>
      <span style="font-size:16.5px">Women Over 40</span>
      <span style="font-size:19px">Are Using To</span>
      <span style="font-size:17px">Get Snatched;</span>
      <span style="font-size:13.5px">Without Starving.</span>
      <span style="font-size:15.5px">Comment Skinny</span>
      <span style="font-size:23px">To Get The</span>
      <span style="font-size:21px">Exact Plan.</span>
    </p>
    <p class="handle">@TovaMarshOnline</p>
  </article>

  <article class="post row-1 col-4">
    <p class="quote quote--humanist">
      <span style="font-size:19px">You’re Doing</span>
      <span style="font-size:34px;font-weight:600">All The</span>
      <span style="font-size:17px">“Right” Things,</span>
      <span style="font-size:17px">But Your Belly</span>
      <span style="font-size:16px">Won’t Go Down?</span>
      <span style="font-size:20.5px">Here’s What</span>
      <span style="font-size:13.5px">You Haven’t Tried.</span>
    </p>
    <p class="handle">@TovaMarshOnline</p>
  </article>

  <article class="post row-1 col-5">
    <p class="quote">
      <span style="font-size:15.5px">This 90-Day Plan</span>
      <span style="font-size:35px">Helped</span>
      <span style="font-size:17px">Women Over 40</span>
      <span style="font-size:23px">Slim Down,</span>
      <span style="font-size:16px">Get A Tiny Waist</span>
      <span style="font-size:12.3px">And Feel Sexy Again.</span>
      <span style="font-size:20.5px">You’re Next.</span>
    </p>
    <p class="handle">@TovaMarshOnline</p>
  </article>

  <article class="post row-2 col-1">
    <p class="quote">
      <span style="font-size:23.5px">Bloating.</span>
      <span style="font-size:20px">Muffin Top.</span>
      <span style="font-size:13.5px">Puffy Waistline.</span>
      <span style="font-size:18px">Your Body’s</span>
      <span style="font-size:15.5px">Screaming For</span>
      <span style="font-size:19px">A Different</span>
      <span style="font-size:19.5px">Kind Of Fix.</span>
      <span style="font-size:23px">Here It Is</span>
    </p>
    <p class="handle">@TovaMarshOnline</p>
  </article>

  <article class="post row-2 col-2">
    <p class="quote quote--humanist">
      <span style="font-size:24px">Flat Tummy</span>
      <span style="font-size:22px">In Your 40s?</span>
      <span style="font-size:15px">It’s Still Possible!</span>
      <span style="font-size:28px">Comment</span>
      <span style="font-size:22px">Bye Belly To</span>
      <span style="font-size:14.5px">Get The 10 Secrets</span>
      <span style="font-size:21.5px">To A Flatter</span>
      <span style="font-size:37px;font-weight:600">Tummy</span>
    </p>
    <p class="handle">@TovaMarshOnline</p>
  </article>

  <article class="post row-2 col-3">
    <p class="quote">
      <span style="font-size:16.5px">The Stubborn</span>
      <span style="font-size:12px">Belly Fat After 40?</span>
      <span style="font-size:16px">It’s Not About</span>
      <span style="font-size:24px">Calories;</span>
      <span style="font-size:14.5px">It’s About Your</span>
      <span style="font-size:21.5px">Hormones.</span>
      <span style="font-size:15px">Here Is The Fix!</span>
    </p>
    <p class="handle">@TovaMarshOnline</p>
  </article>

  <article class="post row-2 col-4">
    <p class="quote">
      <span style="font-size:21px">Your Belly</span>
      <span style="font-size:25px">Isn’t Fat...</span>
      <span style="font-size:16px">It’s Hormonal.</span>
      <span style="font-size:21px">And Here’s</span>
      <span style="font-size:16.5px">How To Fix It.</span>
      <span style="font-size:12.5px">Comment Hormones</span>
      <span style="font-size:18.5px">If Nothing Is</span>
      <span style="font-size:25px">Working.</span>
    </p>
    <p class="handle">@TovaMarshOnline</p>
  </article>

  <article class="post row-2 col-5">
    <p class="quote">
      <span style="font-size:14px">That Stubborn</span>
      <span style="font-size:25px">Weight?</span>
      <span style="font-size:28px">It’s Not</span>
      <span style="font-size:19px">Your Fault.</span>
      <span style="font-size:14.5px">Your Hormones</span>
      <span style="font-size:17px">Are To Blame</span>
      <span style="font-size:19.5px">And You’re</span>
      <span style="font-size:19.5px">Not Alone;</span>
      <span style="font-size:12px">But There Is A Fix.</span>
    </p>
    <p class="handle">@TovaMarshOnline</p>
  </article>

</main>
</body>
</html>
```